Brightpath Letterhead

We would like a letterhead for our company. I have uploaded our logo.

Brightpath Ridge Consulting
1450 W Corliss Ave Ste 310
Arlington, TX 76006
833-517-2906

```html
<!DOCTYPE html>
<html lang="en">
<head>
<meta charset="utf-8">
<title>Brightpath Ridge Consulting — Letterhead</title>
<link rel="stylesheet" href="https://fonts.googleapis.com/css2?family=Arimo:wght@400&family=Jost:wght@600&family=Mulish:wght@700&display=swap">
<style>
  :root {
    --teal-deep: #005e6e;
    --mint: #6cc59a;
    --ink: #4f4f52;
    --paper: #fbfbfc;
    --stage: #d9d9db;
    --signature-tone: #e6e8ea;
  }
  html, body {
    margin: 0;
    width: 1200px;
    height: 1079px;
    overflow: hidden;
    background: var(--stage);
  }
  .letterhead {
    position: absolute;
    left: 267px;
    top: 70px;
    width: 1121px;
    height: 1585px;
    background: var(--paper);
    transform: scale(0.5932);
    transform-origin: top left;
    overflow: hidden;
  }
  .header-band {
    position: absolute;
    left: 0;
    top: 0;
    width: 1121px;
    height: 135px;
    background: linear-gradient(to bottom, var(--teal-deep) 0%, var(--teal-deep) 35%, var(--mint) 75%, var(--paper) 100%);
  }
  .brand {
    position: absolute;
    left: 100px;
    top: 150px;
    display: flex;
    align-items: center;
    gap: 16px;
  }
  .brand-dot {
    width: 52px;
    height: 52px;
    border-radius: 50%;
    background: var(--teal-deep);
  }
  .brand-name {
    font-family: "Jost", sans-serif;
    font-weight: 600;
    color: var(--teal-deep);
    font-size: 30px;
    line-height: 32px;
    letter-spacing: 3px;
    text-transform: uppercase;
  }
  .letter-body {
    position: absolute;
    left: 100px;
    top: 488px;
    width: 980px;
    color: var(--ink);
  }
  .salutation {
    font-family: "Mulish", sans-serif;
    font-weight: 700;
    font-size: 26px;
    margin: 0 0 44px 2px;
  }
  .letter-body p.copy {
    font-family: "Arimo", sans-serif;
    font-size: 18.6px;
    line-height: 23px;
    margin: 0 0 20px;
    white-space: nowrap;
  }
  .closing {
    position: absolute;
    left: 102px;
    top: 1036px;
    margin: 0;
    font-family: "Mulish", sans-serif;
    font-weight: 700;
    font-size: 15px;
    color: var(--ink);
  }
  .signature {
    position: absolute;
    left: 101px;
    top: 1100px;
    width: 185px;
    height: 58px;
    background: var(--signature-tone);
  }
  .footer-contact {
    position: absolute;
    left: 0;
    right: 0;
    top: 1524px;
    text-align: center;
    font-family: "Arimo", sans-serif;
    font-size: 17.5px;
    color: var(--ink);
  }
  .footer-contact .phone-icon {
    width: 14px;
    height: 14px;
    vertical-align: -1px;
    margin-right: 4px;
  }
  .footer-contact .divider { margin: 0 14px; }
</style>
</head>
<body>
  <main class="letterhead">
    <div class="header-band" role="img" aria-label="Decorative teal and mint header artwork"></div>

    <div class="brand">
      <span class="brand-dot"></span>
      <div class="brand-name">Brightpath Ridge<br>Consulting</div>
    </div>

    <section class="letter-body">
      <p class="salutation">Dear Mr. Whitaker,</p>
      <p class="copy">Lorem ipsum dolor sit amet, consectetuer adipiscing elit, sed diam nonmmy nibh euismod tincidunt ut laor<br>eet dolore magna aliquam erat volutpat. Ut wisi enim ad minim veniam, quis nostrud exerci tationmcorper<br>suscipit lobortis nisl ut aliquip ex ea commodo consequat. Duis autem vel eum iriure dolor in hendrerit in<br>vulputate velit esse molestie consequat, vel illum dolore eu feugiat</p>
      <p class="copy">Rorem ipsum dolor sit amet, consectetuer adipiscing elit, sed diam nonmmy nibh euismod tincidunt ut laor<br>eet dolore magna aliquam erat volutpat. Ut wisi enim ad minim veniam, quis nostrud exerci tationmcorper<br>suscipit lobortis nisl ut aliquip ex ea commodo consequat. Duis autem vel eum iriure dolor in hendrerit in<br>vulputate velit esse molest</p>
      <p class="copy">Dorem ipsum dolor sit amet, consectetuer adipiscing elit, sed diam nonmmy nibh euismod tincidunt ut laor<br>eet dolore magna aliquam erat volutpat. Ut wisi enim ad minim veniam, quis nostrud exerci tationmcorper<br>suscipit lobortis nisl ut aliquip ex ea commodo consequat. Duis autem vel eum iriure dolor in hendrerit in<br>suscipit lobortis nisl ut aliquip ex ea commodo consequat. Duis autem vel eum iriure dolor in hendrerit in<br>vulputate velit esse molestie consequat, vel illum</p>
      <p class="copy">Sorem ipsum dolor sit amet, consectetuer adipiscing elit, sed diam nonmmy nibh euismod tincidunt ut laor<br>eet dolore magna aliquam erat volutpat. Ut wisi enim ad minim veniam, quis nostrud exerci tationmcorper<br>suscipit lobortis nisl ut aliquip ex ea commodo consequat. Duis autem vel eum iriure dolor in</p>
    </section>

    <p class="closing">Sincerely,</p>
    <div class="signature" role="img" aria-label="Handwritten signature of the sender"></div>

    <footer class="footer-contact">
      <svg class="phone-icon" viewBox="0 0 24 24" aria-hidden="true"><path fill="var(--mint)" d="M6.6 10.8a15.1 15.1 0 0 0 6.6 6.6l2.2-2.2a1 1 0 0 1 1-.25 11.4 11.4 0 0 0 3.6.57 1 1 0 0 1 1 1V20a1 1 0 0 1-1 1A17 17 0 0 1 3 4a1 1 0 0 1 1-1h3.5a1 1 0 0 1 1 1c0 1.25.2 2.450.57 3.6a1 1 0 0 1-.25 1z"/></svg>833-517-2906<span class="divider">|</span>1450 W Corliss Ave, Ste 310, Arlington, TX 76006
    </footer>
  </main>
</body>
</html>
```